create a webpage for optometry practice

I'm looking to create a professional and elegant webpage for my practice. I prefer neutral earthy colors, but I am open to other ideas. I have included an image of my logo to be used in the process. This will be a page that will illustrate information about my practice and the kind of services we offer. I am in process of having the practice remodeled. So I don't have any photos of my practice to include yet.

Target Market(s)

My practice serves young and mature families.

Font styles to use
Sans Serif

Colors
33a6d7
86cfc6
85cae6
cadf82
3276b5
faa54b
abd036
f78c1e

Requirements
Must have
• I would need to incorporate information about my practice, services, insurance accepted, make appointment, contact us, and about our family.
Nice to have
• I would like to see something fresh, modern, and unique

```html
<!DOCTYPE html>
<html lang="en">
<head>
<meta charset="utf-8">
<title>Lumen Eye Care</title>
<link href="https://fonts.googleapis.com/css2?family=Open+Sans:wght@300;400;600;700;800&family=Oswald:wght@300&display=swap" rel="stylesheet">
<style>
:root{
  --page:#ffffff;
  --ink:#1d1d1f;
  --text:#444;
  --blue:#3276b5;
  --orange:#faa54b;
  --orange-deep:#f78c1e;
  --teal:#86cfc6;
  --green:#cadf82;
  --soft:#f4f3f4;
  --dark:#32353d;
  --accent:#cadf82;
  --line:#9fbcd6;
}
*{margin:0;padding:0;box-sizing:border-box}
html,body{width:1200px;height:900px;overflow:hidden;background:var(--page);font-family:"Open Sans",sans-serif;color:var(--text)}
.page{position:absolute;left:252px;top:0;width:698px;height:900px;background:var(--page);overflow:hidden}
.abs{position:absolute}

/* hero */
.hero{left:0;top:0;width:698px;height:306px;background:#fff}
.hero-photo{left:300px;top:0;width:398px;height:305px;
  background:
    radial-gradient(ellipse 70px 55px at 240px 160px,rgba(70,120,190,.55),rgba(70,120,190,0) 100%),
    linear-gradient(90deg,#fff 0%,#f1f1f1 18%,#dedede 45%,#c9c9c9 75%,#b4b4b4 100%)}
.hero-line{left:0;top:305px;width:698px;height:1px;background:var(--line)}
.nav-band{left:200px;top:0}
.brand{left:93px;top:38px;display:flex;align-items:center;gap:6px;font-size:19px;font-weight:400;color:#555;letter-spacing:-0.5px}
.brand-dot{width:11px;height:11px;border-radius:50%;background:var(--orange)}
.nav{left:329px;top:16px;display:flex;font-size:5.8px;font-weight:600;color:#222;text-transform:uppercase;white-space:nowrap}
.nav a{color:inherit;text-decoration:none;padding:9px 0 0;height:48px}
.nav a.active{background:var(--orange-deep);color:#fff;width:24px;text-align:center}
.call{left:456px;top:37px;color:#fff;font-weight:700;font-size:14px;letter-spacing:-0.3px}
.headline{left:93px;top:172px;width:175px;height:95px}
.hl-1{position:absolute;left:0;top:0;font-family:"Oswald",sans-serif;font-weight:300;font-size:37px;line-height:37px;color:var(--ink);letter-spacing:-1.6px;white-space:nowrap}
.hl-for{position:absolute;left:154px;top:30px;font-size:8px;font-style:normal;color:var(--ink)}
.hl-2{position:absolute;left:0;top:34px;font-weight:800;font-size:31px;line-height:31px;color:var(--ink);letter-spacing:1.6px}
.hl-3{position:absolute;left:0;top:62px;font-weight:800;font-size:31px;line-height:31px;color:var(--blue);letter-spacing:9.2px}
.arrows{left:574px;top:284px;display:flex;gap:4px}

/* about */
.about{left:0;top:306px;width:698px;height:281px;background:var(--soft)}
.about-img{left:104px;top:44px;width:205px;height:192px;border-radius:40px 40px 60px 60px;background:radial-gradient(circle at 50% 55%,#d8dadd,#b9bcc0 60%,#f4f3f4 72%)}
.about-title{left:349px;top:70px;font-size:24px;font-weight:300;color:var(--blue);letter-spacing:-0.3px}
.about-copy{left:349px;top:111px;width:240px;font-size:6.3px;line-height:12.7px;color:#333}
.btn{left:349px;top:206px;width:43px;height:16px;background:var(--blue);color:#fff;font-size:5px;text-align:center;line-height:16px;text-transform:uppercase}
.rule{left:0;top:587px;width:698px;height:1px;background:#c9d3dd}

/* tiles */
.tile{position:absolute;color:#fff}
.t-family{left:0;top:591px;width:237px;height:159px;background:var(--orange)}
.t-family .divider{position:absolute;left:94px;top:0;width:1px;height:159px;background:rgba(255,255,255,.6)}
.t-services{left:239px;top:591px;width:192px;height:106px;background:var(--blue)}
.t-insurance{left:239px;top:699px;width:192px;height:51px;background:var(--teal)}
.t-appoint{left:433px;top:591px;width:265px;height:159px;background:var(--green)}
.t-appoint .divider{position:absolute;left:171px;top:0;width:1px;height:159px;background:rgba(255,255,255,.7)}
.tile-title{position:absolute;font-size:18px;font-weight:300;display:flex;align-items:center;gap:7px;white-space:nowrap}
.tile-copy{position:absolute;font-size:6.1px;line-height:12.9px}
.appt-title{left:14px;top:12px;font-size:16.5px;font-weight:400;letter-spacing:-0.3px;color:var(--ink);position:absolute;white-space:nowrap}
.field{position:absolute;left:15px;width:140px;height:18px;background:#fff;font-size:6.5px;color:#999;text-align:center;line-height:18px}
.submit{position:absolute;left:15px;top:121px;width:141px;height:33px;border:1px solid #555;font-size:10px;color:#222;text-align:center;line-height:31px}

/* footer */
.footer{left:0;top:752px;width:698px;height:148px;background:var(--dark);color:#fff}
.connector{left:123px;top:0;width:4px;height:24px;background:#fff}
.badge{left:94px;top:23px;width:62px;height:62px;border-radius:50%;background:#fff;display:flex;align-items:center;justify-content:center;font-size:9px;color:#555;text-align:center;line-height:1.1}
.f-label{font-size:7px;font-weight:700;color:var(--accent);text-transform:uppercase}
.f-value{font-size:5px;font-weight:600;letter-spacing:.1px;margin-top:6px;text-transform:uppercase;white-space:nowrap}
.f-sep{width:1px;height:20px;background:#777}
.follow{left:176px;top:89px;display:flex;align-items:center;gap:6px}
.social{width:14px;height:14px;border-radius:50%;border:1px solid #999}
.follow-line{width:30px;height:1px;background:#999;margin-left:6px}
.fnav{display:flex;gap:15px;font-size:5.5px;font-weight:400;text-transform:uppercase;margin-left:4px;white-space:nowrap}
.f-rule{left:94px;top:132px;width:510px;height:1px;background:#4a4d55}
.copyright{left:0;top:137px;width:698px;text-align:center;font-size:4.5px;color:#aaa}
</style>
</head>
<body>
<div class="page">

  <header class="hero abs">
    <div class="hero-photo abs" role="img" aria-label="Black and white close-up photograph of a woman's eye with a bright blue iris"></div>
    <svg class="nav-band abs" width="498" height="64" aria-hidden="true">
      <polygon points="0,0 498,0 498,64 58,64" fill="#d9d9d9" opacity=".75"/>
    </svg>
    <div class="hero-line abs"></div>
    <div class="brand abs"><span class="brand-dot"></span>LUMEN EYE CARE</div>
    <nav class="nav abs">
      <a class="active" href="#">Home</a>
      <a href="#" style="margin-left:12px">About us</a>
      <a href="#" style="margin-left:15px">Treatments</a>
      <a href="#" style="margin-left:15px">FAQ</a>
      <a href="#" style="margin-left:13px">Our services</a>
      <a href="#" style="margin-left:13px">Lenses</a>
      <a href="#" style="margin-left:13px">Contact us</a>
    </nav>
    <div class="call abs">CALL US: 0100-555-246</div>
    <h1 class="headline abs">
      <span class="hl-1">HEALTHY EYES</span>
      <span class="hl-for">for</span>
      <span class="hl-2">HEALTHY</span>
      <span class="hl-3">VISION</span>
    </h1>
    <div class="arrows abs">
      <svg width="13" height="13" viewBox="0 0 13 13"><circle cx="6.5" cy="6.5" r="6.5" fill="#8fa6bd"/><path d="M7.5 3.8 4.8 6.5 7.5 9.2" stroke="#fff" stroke-width="1.4" fill="none"/></svg>
      <svg width="13" height="13" viewBox="0 0 13 13"><circle cx="6.5" cy="6.5" r="6.5" fill="#8fa6bd"/><path d="M5.5 3.8 8.2 6.5 5.5 9.2" stroke="#fff" stroke-width="1.4" fill="none"/></svg>
    </div>
  </header>

  <section class="about abs">
    <div class="about-img abs" role="img" aria-label="Photograph of a silver optometry phoropter eye testing instrument"></div>
    <h2 class="about-title abs">About my Practice</h2>
    <p class="about-copy abs">Nulla facilisi. Phasellus euismod neque ac efficitur ultricies. Maecenas auctor, ipsum ac volutpat posuere, lacus elit blandit ante, eu sodales lectus lacus vel lorem. Suspendisse aliquam dolor eu est pretium, eget posuere neque egestas. Quisque in purus ligula. Maecenas magna velit, tincidunt eget iaculis rutrum, gravida vitae massa. Duis a ipsum interdum, suscipit massa nec, lacinia lorem. Quisque tortor nunc, semper vel placerat eget, tincidunt et odio.</p>
    <div class="btn abs">Read more</div>
  </section>
  <div class="rule abs"></div>

  <section class="tile t-family">
    <div class="divider"></div>
    <h3 class="tile-title" style="left:109px;top:12px">Our Family
      <svg width="11" height="11" viewBox="0 0 11 11"><circle cx="5.5" cy="5.5" r="5.5" fill="#fff"/><path d="M4.5 3 7 5.5 4.5 8" stroke="#faa54b" stroke-width="1.5" fill="none"/></svg></h3>
    <p class="tile-copy" style="left:111px;top:41px;width:116px">Nulla facilisi. Phasellus euismod neque ac efficitur ultricies. Maecenas auctor, ipsum ac volutpat posuere, lacus elit blandit ante, eu sodales lectus lacus vel lorem. Suspendisse aliquam dolor eu est pretium, eget posuere neque egestas. Quisque in purus ligula.</p>
  </section>

  <section class="tile t-services">
    <h3 class="tile-title" style="left:13px;top:11px">Services
      <svg width="11" height="11" viewBox="0 0 11 11"><circle cx="5.5" cy="5.5" r="5.5" fill="#fff"/><path d="M4.5 3 7 5.5 4.5 8" stroke="#3276b5" stroke-width="1.5" fill="none"/></svg></h3>
    <p class="tile-copy" style="left:14px;top:41px;width:165px">Nulla facilisi. Phasellus euismod neque ac efficitur ultricies. Maecenas auctor, ipsum ac volutpat posuere, lacus elit blandit ante, eu sodales lectus lacus vel lorem. Suspendisse aliquam dolor eu est pretium.</p>
  </section>

  <section class="tile t-insurance">
    <h3 class="tile-title" style="left:14px;top:13px;font-size:17px">Insurance Accepted
      <svg width="11" height="11" viewBox="0 0 11 11"><circle cx="5.5" cy="5.5" r="5.5" fill="#fff"/><path d="M4.5 3 7 5.5 4.5 8" stroke="#86cfc6" stroke-width="1.5" fill="none"/></svg></h3>
  </section>

  <section class="tile t-appoint">
    <div class="divider"></div>
    <h3 class="appt-title">Make Appointment</h3>
    <div class="field" style="top:48px">--NAME--</div>
    <div class="field" style="top:70px">--EMAIL--</div>
    <div class="field" style="top:92px">--PHONE--</div>
    <div class="submit">SUBMIT</div>
  </section>

  <footer class="footer abs">
    <div class="connector abs"></div>
    <div class="badge abs">LUMEN<br>EYE CARE</div>
    <div class="abs" style="left:177px;top:45px">
      <div class="f-label">Our clinic</div>
      <div class="f-value">Clinic Office, 210 Fernhill Lane, Glasgow G12 8QQ</div>
    </div>
    <div class="f-sep abs" style="left:387px;top:45px"></div>
    <div class="abs" style="left:395px;top:45px">
      <div class="f-label">Call us</div>
      <div class="f-value" style="letter-spacing:1.5px">0100-555-246</div>
    </div>
    <div class="f-sep abs" style="left:487px;top:45px"></div>
    <div class="abs" style="left:528px;top:45px">
      <div class="f-label">E mail</div>
      <div class="f-value" style="text-transform:none;letter-spacing:.5px">hello@lumeneyes.example</div>
    </div>
    <div class="follow abs">
      <span class="f-label">Follow us:</span>
      <span class="social" style="margin-left:4px"></span><span class="social"></span><span class="social"></span>
      <span class="follow-line"></span>
      <nav class="fnav"><span>Home</span><span>About us</span><span>Treatments</span><span>FAQ</span><span>Our services</span><span>Lenses</span><span>Contact us</span></nav>
    </div>
    <div class="f-rule abs"></div>
    <div class="copyright abs">© 2015 All Rights Reserved</div>
  </footer>

</div>
</body>
</html>
```